Upgrade UI for an existing app

I have an app that is already in the appstore, and I have finally get to the point where the app is fairly complete in its user flow and app features.

I would like to take the app to the next level, and completely revamp its look and feel, to give it that flat iOS7 look.

The app can be downloaded at https://apps.vendrulo.example/us/app/brindle-kto/id574093186?mt=8

And you can log into the app using the credential below:

sketch.harbor
password

I am also open to new ideas around UX, but my biggest focus is on getting the UI updated, especially for the setting page, support page, and about page.

Thanks,

Rob

Majority of the submissions are for iPhone, whereas I was hoping for more iPad redesign.

I think the issue is that, a lot of people didn't download the app from appstore.

I have uploaded two zip files with iPad screenshot.  Please submit a few designs that are based off the existing iPad screenshot.

```html
<!DOCTYPE html>
<html lang="en">
<head>
<meta charset="utf-8">
<title>Questions</title>
<link rel="stylesheet" href="https://fonts.googleapis.com/css2?family=Lato:wght@300;400&display=swap">
<style>
  :root {
    --bar-dark: #2b2f33;
    --legend-teal: #33c9a0;
    --legend-divider: #e6f7f2;
    --page-bg: #e8fafc;
    --section-rule: #20b48e;
    --ink: #2c3236;
    --axis: #23292d;
    --score-green: #3d9640;
    --average-blue: #2f93f0;
    --white: #ffffff;
  }
  * { box-sizing: border-box; margin: 0; padding: 0; }
  html, body { width: 676px; height: 1200px; overflow: hidden; background: var(--page-bg); }
  body { font-family: "Lato", "Helvetica Neue", Arial, sans-serif; color: var(--ink); }

  .screen { position: relative; width: 676px; height: 1200px; overflow: hidden; background: var(--page-bg); }

  .status-bar {
    position: absolute; left: 0; top: 0; width: 676px; height: 42px;
    background: var(--bar-dark); color: var(--white);
    font-size: 22px; font-weight: 400; line-height: 1;
  }
  .status-bar .carrier { position: absolute; left: 12px; top: 10px; display: flex; align-items: center; gap: 6px; }
  .status-bar .time { position: absolute; left: 0; right: 0; top: 10px; text-align: center; font-size: 23px; }
  .status-bar .power { position: absolute; right: 10px; top: 10px; display: flex; align-items: center; gap: 8px; }

  .nav-bar {
    position: absolute; left: 0; top: 42px; width: 676px; height: 104px;
    background: var(--bar-dark); color: var(--white);
  }
  .nav-bar .back { position: absolute; left: 12px; top: 30px; }
  .nav-bar .title {
    position: absolute; left: 0; right: 0; top: 24px; text-align: center;
    font-size: 49px; font-weight: 300; letter-spacing: 0.5px; line-height: 1.2;
  }

  .legend {
    position: absolute; left: 0; top: 148px; width: 676px; height: 80px;
    background: var(--legend-teal); display: flex; color: var(--white);
  }
  .legend-item {
    flex: 1; display: flex; align-items: center; justify-content: center; gap: 14px;
    font-size: 29px; font-weight: 400;
  }
  .legend-item + .legend-item { border-left: 1px solid var(--legend-divider); }
  .legend-swatch { width: 47px; height: 47px; border-radius: 50%; border: 1.5px solid var(--white); }
  .swatch-score { background: var(--score-green); }
  .swatch-average { background: var(--average-blue); }

  .results { position: absolute; left: 0; top: 228px; width: 676px; }
  .result-section {
    position: relative; height: 271.5px;
    border-bottom: 1px solid var(--section-rule);
  }
  .result-title {
    position: absolute; left: 63px; top: 17px;
    font-size: 29.5px; font-weight: 400; line-height: 1.2;
  }
  .result-summary {
    position: absolute; left: 63px; top: 51px;
    font-size: 17.5px; font-weight: 400; line-height: 1.2;
  }
  .result-chart { position: absolute; left: 0; top: 101px; width: 676px; height: 158px; }
  .result-chart text { font-family: "Lato", "Helvetica Neue", Arial, sans-serif; font-size: 17px; fill: var(--ink); }
</style>
</head>
<body>
<div class="screen">

  <div class="status-bar">
    <div class="carrier">
      <svg width="82" height="14" viewBox="0 0 82 14" aria-hidden="true">
        <circle cx="7" cy="7" r="6" fill="#fff"/>
        <circle cx="24" cy="7" r="6" fill="#fff"/>
        <circle cx="41" cy="7" r="6" fill="#fff"/>
        <circle cx="58" cy="7" r="5.3" fill="none" stroke="#fff" stroke-width="1.3"/>
        <circle cx="75" cy="7" r="5.3" fill="none" stroke="#fff" stroke-width="1.3"/>
      </svg>
      <span>VEXA</span>
      <svg width="26" height="20" viewBox="0 0 26 20" aria-hidden="true">
        <path d="M13 18 L9 14 A6 6 0 0 1 17 14 Z" fill="#fff"/>
        <path d="M5 10 A11 11 0 0 1 21 10" fill="none" stroke="#fff" stroke-width="2.6"/>
        <path d="M1 6 A17 17 0 0 1 25 6" fill="none" stroke="#fff" stroke-width="2.6"/>
      </svg>
    </div>
    <div class="time">4:21 PM</div>
    <div class="power">
      <span>100%</span>
      <svg width="50" height="22" viewBox="0 0 50 22" aria-hidden="true">
        <rect x="1" y="1" width="43" height="20" rx="3" fill="none" stroke="#fff" stroke-width="1.6"/>
        <rect x="4" y="4" width="37" height="14" rx="1" fill="#fff"/>
        <rect x="45" y="7" width="3" height="8" rx="1" fill="#fff"/>
      </svg>
    </div>
  </div>

  <div class="nav-bar">
    <svg class="back" width="30" height="52" viewBox="0 0 30 52" aria-label="Back" role="img">
      <path d="M26 2 L4 26 L26 50" fill="none" stroke="#fff" stroke-width="4" stroke-linecap="round" stroke-linejoin="round"/>
    </svg>
    <h1 class="title">Questions</h1>
  </div>

  <div class="legend">
    <div class="legend-item">Your Score <span class="legend-swatch swatch-score"></span></div>
    <div class="legend-item">Class Average <span class="legend-swatch swatch-average"></span></div>
  </div>

  <div class="results">
    <section class="result-section">
      <h2 class="result-title">Overall</h2>
      <p class="result-summary">64 of 125 correct (51.20 %)</p>
      <svg class="result-chart" viewBox="0 0 640 150" aria-label="Your score 52%, class average 80%" role="img">
        <rect x="62" y="22" width="247" height="32" fill="var(--score-green)"/>
        <rect x="62" y="66" width="377" height="32" fill="var(--average-blue)"/>
        <rect x="59.5" y="2" width="3" height="110" fill="var(--axis)"/>
        <rect x="59.5" y="109" width="521" height="3" fill="var(--axis)"/>
        <text x="61" y="141" text-anchor="middle">0%</text>
        <text x="176" y="141" text-anchor="middle">25%</text>
        <text x="292" y="141" text-anchor="middle">50%</text>
        <text x="408" y="141" text-anchor="middle">75%</text>
        <text x="533" y="141" text-anchor="middle">100%</text>
      </svg>
    </section>

    <section class="result-section">
      <h2 class="result-title">Overall</h2>
      <p class="result-summary">64 of 125 correct (51.20 %)</p>
      <svg class="result-chart" viewBox="0 0 640 150" aria-label="Your score 52%, class average 80%" role="img">
        <rect x="62" y="22" width="247" height="32" fill="var(--score-green)"/>
        <rect x="62" y="66" width="377" height="32" fill="var(--average-blue)"/>
        <rect x="59.5" y="2" width="3" height="110" fill="var(--axis)"/>
        <rect x="59.5" y="109" width="521" height="3" fill="var(--axis)"/>
        <text x="61" y="141" text-anchor="middle">0%</text>
        <text x="176" y="141" text-anchor="middle">25%</text>
        <text x="292" y="141" text-anchor="middle">50%</text>
        <text x="408" y="141" text-anchor="middle">75%</text>
        <text x="533" y="141" text-anchor="middle">100%</text>
      </svg>
    </section>

    <section class="result-section">
      <h2 class="result-title">Overall</h2>
      <p class="result-summary">64 of 125 correct (51.20 %)</p>
      <svg class="result-chart" viewBox="0 0 640 150" aria-label="Your score 52%, class average 80%" role="img">
        <rect x="62" y="22" width="247" height="32" fill="var(--score-green)"/>
        <rect x="62" y="66" width="377" height="32" fill="var(--average-blue)"/>
        <rect x="59.5" y="2" width="3" height="110" fill="var(--axis)"/>
        <rect x="59.5" y="109" width="521" height="3" fill="var(--axis)"/>
        <text x="61" y="141" text-anchor="middle">0%</text>
        <text x="176" y="141" text-anchor="middle">25%</text>
        <text x="292" y="141" text-anchor="middle">50%</text>
        <text x="408" y="141" text-anchor="middle">75%</text>
        <text x="533" y="141" text-anchor="middle">100%</text>
      </svg>
    </section>

    <section class="result-section">
      <h2 class="result-title">Overall</h2>
      <p class="result-summary">64 of 125 correct (51.20 %)</p>
      <svg class="result-chart" viewBox="0 0 640 150" aria-label="Your score 52%, class average 80%" role="img">
        <rect x="62" y="22" width="247" height="32" fill="var(--score-green)"/>
        <rect x="62" y="66" width="377" height="32" fill="var(--average-blue)"/>
        <rect x="59.5" y="2" width="3" height="110" fill="var(--axis)"/>
        <rect x="59.5" y="109" width="521" height="3" fill="var(--axis)"/>
        <text x="61" y="141" text-anchor="middle">0%</text>
        <text x="176" y="141" text-anchor="middle">25%</text>
        <text x="292" y="141" text-anchor="middle">50%</text>
        <text x="408" y="141" text-anchor="middle">75%</text>
        <text x="533" y="141" text-anchor="middle">100%</text>
      </svg>
    </section>
  </div>

</div>
</body>
</html>
```